Figure for a research paper

I am working on designing a figure for a research paper that illustrates the effect of KADO Pathways assessment on student outcomes over time by impacting teacher bias and teacher perception of student growth. I built the attached figure via powerpoint. It includes the very basic elements but it does not look great and I am not sure that it is clearly depicting what I am hoping to illustrate. I would like for you to build an illustration of this idea that i can include in the paper.

```html
<!DOCTYPE html>
<html lang="en">
<head>
<meta charset="utf-8">
<title>KADO Framework Assessment – Effect on SEL Program Effectiveness Over Time</title>
<link href="https://fonts.googleapis.com/css2?family=Montserrat:wght@400;600;700&display=swap" rel="stylesheet">
<style>
  :root {
    --canvas: #ffffff;
    --ink: #555a60;
    --axis: #4f5359;
    --assessment-zone: #d8f1fa;
    --perception-zone: #fbe9d6;
    --assessment-line: #3dbfea;
    --teacher-line: #f0952a;
    --divider: #6b6f75;
    --lift: #5ac6ee;
    --bias: #efad5c;
  }
  html, body {
    margin: 0;
    padding: 0;
    width: 1200px;
    height: 815px;
    overflow: hidden;
    background: var(--canvas);
  }
  .figure {
    display: block;
    width: 1200px;
    height: 815px;
    font-family: "Montserrat", "Helvetica Neue", Arial, sans-serif;
  }
  .zone-assessment { fill: var(--assessment-zone); }
  .zone-perception { fill: var(--perception-zone); }
  .axis { stroke: var(--axis); stroke-width: 1.6; fill: none; }
  .axis-head { fill: var(--axis); }
  .trend-assessment { stroke: var(--assessment-line); stroke-width: 2.6; }
  .trend-teacher { stroke: var(--teacher-line); stroke-width: 2.6; }
  .trend-true { stroke: var(--divider); stroke-width: 1.3; stroke-dasharray: 3 4; }
  .arrow-lift { fill: url(#liftFade); }
  .arrow-bias { fill: url(#biasFade); }
  .label { fill: var(--ink); font-size: 17px; font-weight: 400; }
  .label-strong { fill: var(--ink); font-size: 18px; font-weight: 700; }
  .axis-title { fill: #2f3236; font-size: 18px; font-weight: 700; }
  .axis-subtitle { fill: var(--ink); font-size: 17px; font-weight: 400; }
</style>
</head>
<body>
<svg class="figure" viewBox="0 0 1200 815" xmlns="http://www.w3.org/2000/svg" role="img" aria-label="Chart: effectiveness of the SEL program on the student over time, comparing the KADO Framework Assessment trend with teacher bias and teacher perception of growth">
  <defs>
    <linearGradient id="liftFade" x1="0" y1="0" x2="0" y2="1">
      <stop offset="0" stop-color="var(--lift)" stop-opacity="1"/>
      <stop offset="1" stop-color="var(--lift)" stop-opacity="0.05"/>
    </linearGradient>
    <linearGradient id="biasFade" x1="0" y1="0" x2="0" y2="1">
      <stop offset="0" stop-color="var(--bias)" stop-opacity="0.05"/>
      <stop offset="1" stop-color="var(--bias)" stop-opacity="1"/>
    </linearGradient>
  </defs>

  <!-- plot zones -->
  <rect class="zone-assessment" x="265" y="170" width="720" height="436"/>
  <polygon class="zone-perception" points="265,510 985,326 985,606 265,606"/>

  <!-- trend lines -->
  <line class="trend-true" x1="265" y1="507" x2="985" y2="320"/>
  <line class="trend-assessment" x1="265" y1="507" x2="985" y2="256"/>
  <line class="trend-teacher" x1="265" y1="507" x2="985" y2="379"/>

  <!-- assessment lift arrows -->
  <g class="arrows-lift">
    <polygon class="arrow-lift" points="388,400 420,437 401,437 401,472 375,472 375,437 356,437"/>
    <polygon class="arrow-lift" points="564,339 596,378 577,378 577,433 551,433 551,378 532,378"/>
    <polygon class="arrow-lift" points="737,282 769,320 750,320 750,388 724,388 724,320 705,320"/>
    <polygon class="arrow-lift" points="912,223 944,263 925,263 925,343 899,343 899,263 880,263"/>
  </g>

  <!-- teacher bias arrows -->
  <g class="arrows-bias">
    <polygon class="arrow-bias" points="375,476 401,476 401,514 420,514 388,550 356,514 375,514"/>
    <polygon class="arrow-bias" points="551,446 577,446 577,489 596,489 564,524 532,489 551,489"/>
    <polygon class="arrow-bias" points="724,388 750,388 750,455 769,455 737,492 705,455 724,455"/>
    <polygon class="arrow-bias" points="899,343 925,343 925,423 944,423 912,459 880,423 899,423"/>
  </g>

  <!-- axes -->
  <polyline class="axis" points="265,160 265,606 992,606"/>
  <polygon class="axis-head" points="265,153 257,170 273,170"/>
  <polygon class="axis-head" points="1002,606 985,598 985,614"/>

  <!-- labels -->
  <text class="label-strong" x="624" y="262" text-anchor="middle">KADO Framework Assessment</text>
  <text class="label" x="480" y="582" text-anchor="middle">Teacher Bias</text>
  <text class="label" text-anchor="middle">
    <tspan x="823" y="533">Teacher’s inaccurate</tspan>
    <tspan x="823" y="557">perception of student</tspan>
    <tspan x="823" y="581">growth (or learning)</tspan>
  </text>

  <g class="axis-label-y" transform="translate(221,388) rotate(-90)">
    <text class="axis-title" x="0" y="0" text-anchor="middle">Effectiveness of SEL Program</text>
    <text class="axis-subtitle" x="0" y="23" text-anchor="middle">on the Student</text>
  </g>
  <text class="axis-title" x="622" y="643" text-anchor="middle">Time</text>
</svg>
</body>
</html>
```